Business Card Professional Clean - Ledgerpeak

Create a business card for my company that deals with Cryptocurrencies. I have a few designs ideas that I'd like to be implemented. Thanks! I will include the logo files, and a link to the design styles that I like.

Target Market(s)

Professionals

Industry/Entity Type

Consulting

Contact Information for Business Card

Name: Mark Dunn
Title: CEO/Technical Director
Phone: (587)430-9158
E-mail: mdunn@ledgerpeak.example
Address: Suite 512, 208-3375 Harwood Lane NW

Twitter: @LedgerPeakYYC
Instagram: ledgerpeakyyc

Colors
92b5d7
3276b5
33a6d7
85acd3
85cae6
0592cd

Requirements
Must have
• Some colors that match with the logo and the pictures I put in below.
• Ideally the finished product would look something like the attachments showing the color gradient I want.
Nice to have
• Please see some of the attachments I've included. This is very close to the final product that I would like to see. If someone could recreate something like those I would definitely feel pretty good about it.
• For the instagram and twitter please use the symbols/icon to represent it on the card.
Should not have
• No crazy colors and unprofessional styles. I just want clear info. Don't go outside the boundaries of the colors in the attachment and we should be good. No crazy weird fonts either.

```html
<!DOCTYPE html>
<html lang="en">
<head>
<meta charset="utf-8">
<title>Ledgerpeak Business Card</title>
<link rel="stylesheet" href="https://fonts.googleapis.com/css2?family=Cinzel:wght@400&family=Open+Sans:wght@400&display=swap">
<style>
  :root {
    --stage: #3a3a3c;
    --card-white: #ffffff;
    --brand-blue: #1f63ad;
    --mark-grey: #3c4654;
    --navy-deep: #0b4671;
    --navy-mid: #0d5585;
    --accent-bright: #1a7fd0;
    --accent-clear: rgba(26, 127, 208, 0);
    --text-light: #e8f1f8;
    --text-light-clear: rgba(232, 241, 248, 0);
  }
  * { margin: 0; padding: 0; box-sizing: border-box; }
  html, body { width: 1200px; height: 900px; overflow: hidden; }
  body {
    background: var(--stage);
    display: flex;
    flex-direction: column;
    align-items: center;
    justify-content: center;
    gap: 40px;
  }
  .card {
    width: 640px;
    height: 366px;
    position: relative;
    overflow: hidden;
    border-radius: 2px;
  }
  .card-front {
    background: var(--card-white);
    display: flex;
    align-items: center;
    justify-content: center;
  }
  .brand {
    display: flex;
    align-items: center;
    gap: 16px;
  }
  .brand-square {
    width: 26px;
    height: 26px;
    background: var(--brand-blue);
  }
  .brand-name {
    font-family: "Open Sans", sans-serif;
    font-weight: 400;
    font-size: 42px;
    color: var(--brand-blue);
  }
  .card-back {
    background: linear-gradient(160deg, var(--navy-mid) 0%, var(--navy-deep) 100%);
    color: var(--text-light);
  }
  .tone-left,
  .tone-right {
    position: absolute;
    top: 0;
    height: 100%;
    width: 260px;
  }
  .tone-left {
    left: 0;
    background: radial-gradient(closest-side at 0% 45%, var(--accent-bright) 0%, var(--accent-clear) 100%);
  }
  .tone-right {
    right: 0;
    background: radial-gradient(closest-side at 100% 65%, var(--accent-bright) 0%, var(--accent-clear) 100%);
  }
  .contact {
    position: absolute;
    left: 0; right: 0; top: 88px;
    display: flex;
    flex-direction: column;
    align-items: center;
  }
  .person-name {
    font-family: "Cinzel", serif;
    font-weight: 400;
    font-size: 30px;
    letter-spacing: 1px;
  }
  .person-title {
    font-family: "Open Sans", sans-serif;
    font-size: 14px;
    margin-top: 2px;
  }
  .divider {
    width: 200px;
    height: 1px;
    margin: 14px 0 16px;
    background: linear-gradient(90deg, var(--text-light-clear), var(--text-light), var(--text-light-clear));
  }
  .details {
    font-family: "Open Sans", sans-serif;
    font-size: 14px;
    line-height: 1.75;
    list-style: none;
  }
</style>
</head>
<body>
  <section class="card card-front">
    <div class="brand">
      <span class="brand-square"></span>
      <span class="brand-name">Ledgerpeak</span>
    </div>
  </section>

  <section class="card card-back">
    <div class="tone-left" role="img" aria-label="Blue pixel mosaic accent along the left edge"></div>
    <div class="tone-right" role="img" aria-label="Blue pixel mosaic accent along the right edge"></div>
    <div class="contact">
      <h1 class="person-name">MARK DUNN</h1>
      <p class="person-title">CEO/Technical Director</p>
      <div class="divider"></div>
      <ul class="details">
        <li>P : (587)430-9158 | E : mdunn@ledgerpeak.example</li>
        <li>TW : @LedgerPeakYYC | IN : ledgerpeakyyc</li>
        <li>A : Suite 512, 208-3375 Harwood Lane NW</li>
      </ul>
    </div>
  </section>
</body>
</html>
```